I need a new business card design for my pharmacy.

I need a business card design. I will include my logo.
The card needs to be readable. I prefer to have my logo on one side along with my website, the other side includes the other information. Please use combination of black, neon green, white, and silver. This needs to catch the eye but yet be clearly visible and legible. Thanks

Industry/Entity Type

Pharmacy

Contact Information for Business Card

It needs to have the following information listed:
Mel's Apothecary Owner/Pharm D.
7134 North Brook Lane
Maple Falls, MN 55231
Phone 605-318-6207
Fax 605-318-6209
email: mel@melsapothecary-example.com
www.melsapothecary-example.com
Store hours Monday-Friday 9 am- 6 pm
Saturday 9 am- 1 pm
Sunday Closed
Please utilize the colors black, white, and neon green, maybe silver.

Requirements
Must have
• It needs to be easily readable!
Nice to have
• It should catch the eye.
Should not have
• Do not use any other colors except listed: black, neon green, white, & silver.

```html
<!DOCTYPE html>
<html lang="en">
<head>
<meta charset="utf-8">
<title>Mel's Apothecary – Business Cards</title>
<link rel="stylesheet" href="https://fonts.googleapis.com/css2?family=Open+Sans:wght@400;600&display=swap">
<style>
  :root {
    --black: #232323;
    --ink: #2b2b2b;
    --green: #7ed321;
    --white: #ffffff;
    --silver: #9a9a9a;
    --grey-text: #5a5a5a;
    --bg: #e4e4e4;
  }
  * { box-sizing: border-box; margin: 0; padding: 0; }
  html, body { width: 1200px; height: 873px; overflow: hidden; }
  body {
    background: var(--bg);
    font-family: "Open Sans", Arial, sans-serif;
    display: flex; align-items: center; justify-content: center; gap: 60px;
  }
  .card {
    position: relative; width: 540px; height: 309px;
    background: var(--white); overflow: hidden;
    box-shadow: 0 6px 18px rgba(0,0,0,.18);
  }
  .brand-dot { display: block; border-radius: 50%; background: var(--green); flex: none; }

  /* Contact side */
  .info .brand {
    position: absolute; left: 0; top: 34px; width: 196px;
    display: flex; flex-direction: column; align-items: center; gap: 8px;
    color: var(--ink); font-weight: 600; font-size: 20px; white-space: nowrap;
  }
  .info .brand-dot { width: 20px; height: 20px; }
  .store-hours {
    position: absolute; left: 0; top: 140px; width: 196px; text-align: center;
    font-size: 12px; line-height: 1.6; color: var(--grey-text);
  }
  .contact-panel {
    position: absolute; left: 200px; top: 0; width: 318px; height: 309px; background: var(--black);
  }
  .end-rule { position: absolute; right: 0; top: 0; width: 12px; height: 309px; background: var(--green); }
  .tab {
    position: absolute; left: -14px; width: 28px; background: var(--green);
    display: flex; flex-direction: column; align-items: center; gap: 7px; padding: 8px 0;
  }
  .tab .sep { width: 16px; height: 1px; background: rgba(255,255,255,.75); }
  .tab svg { width: 15px; height: 15px; display: block; }
  .tab-person { top: 26px; }
  .tab-location { top: 146px; }
  .contact-col {
    position: absolute; left: 30px; color: var(--white);
    font-size: 14px; line-height: 1.65; list-style: none; white-space: nowrap;
  }
  .col-owner { top: 24px; }
  .col-owner .caps { text-transform: uppercase; letter-spacing: .3px; }
  .col-address { top: 144px; }

  /* Logo side */
  .front .brand-block {
    position: absolute; left: 0; right: 0; top: 72px;
    display: flex; align-items: center; justify-content: center; gap: 22px;
  }
  .front .brand { color: var(--ink); font-weight: 600; font-size: 34px; white-space: nowrap; }
  .front .brand-dot { width: 24px; height: 24px; }
  .front .divider { width: 1px; height: 60px; background: var(--silver); }
  .band-accent { position: absolute; top: 238px; height: 14px; background: var(--green); }
  .accent-left { left: 0; width: 170px; }
  .accent-right { right: 0; width: 150px; }
  .web-band {
    position: absolute; left: 0; right: 0; top: 252px; bottom: 0; background: var(--black);
    display: flex; align-items: center; justify-content: center;
    color: var(--white); font-size: 16px; letter-spacing: .3px;
  }
</style>
</head>
<body>

  <section class="card info" aria-label="Business card, contact side">
    <div class="brand"><span class="brand-dot"></span>Mel's Apothecary</div>
    <div class="store-hours">
      Store hours<br>
      Monday-Friday 9 am- 6 pm<br>
      Saturday 9 am- 1 pm<br>
      Sunday Closed
    </div>

    <div class="contact-panel">
      <div class="tab tab-person">
        <svg viewBox="0 0 16 16" aria-label="Person"><circle cx="8" cy="5" r="3" fill="#fff"/><path d="M2 15c0-4 3-6 6-6s6 2 6 6z" fill="#fff"/></svg>
        <span class="sep"></span>
        <svg viewBox="0 0 16 16" aria-label="Phone"><path d="M4 1l3 3-2 2c1 2 3 4 5 5l2-2 3 3-2 3C7 15 1 9 1 3z" fill="#fff"/></svg>
      </div>
      <div class="tab tab-location">
        <svg viewBox="0 0 16 16" aria-label="Location"><path d="M8 1a5 5 0 0 0-5 5c0 4 5 9 5 9s5-5 5-9a5 5 0 0 0-5-5z" fill="#fff"/><circle cx="8" cy="6" r="2" fill="#7ed321"/></svg>
        <span class="sep"></span>
        <svg viewBox="0 0 16 16" aria-label="Fax"><rect x="4" y="1" width="8" height="5" fill="#fff"/><rect x="1" y="6" width="14" height="6" rx="1" fill="#fff"/><rect x="4" y="10" width="8" height="5" fill="#fff" stroke="#7ed321"/></svg>
        <span class="sep"></span>
        <svg viewBox="0 0 16 16" aria-label="Email"><rect x="1" y="3" width="14" height="10" fill="#fff"/><path d="M1 3l7 6 7-6" fill="none" stroke="#7ed321" stroke-width="1.4"/></svg>
      </div>

      <ul class="contact-col col-owner">
        <li class="caps">Mel's Apothecary</li>
        <li>Owner/Pharm D.</li>
        <li>605-318-6207</li>
      </ul>
      <ul class="contact-col col-address">
        <li>7134 North Brook Lane</li>
        <li>Maple Falls, MN 55231</li>
        <li>605-318-6209</li>
        <li>mel@melsapothecary-example.com</li>
      </ul>
    </div>
    <div class="end-rule"></div>
  </section>

  <section class="card front" aria-label="Business card, logo side">
    <div class="brand-block">
      <span class="brand-dot"></span>
      <span class="divider"></span>
      <div class="brand">Mel's Apothecary</div>
    </div>
    <div class="band-accent accent-left"></div>
    <div class="band-accent accent-right"></div>
    <div class="web-band">www.melsapothecary-example.com</div>
  </section>

</body>
</html>
```